Rollin’ Kites Copper Tide beer can design

We are not looking for a new logo, we want to use our current logo!! Current Logo is Attached. We want to incorporate our current logo into a full can design for our new non-alcoholic, THC infused Beer design. We cannot use animals or cartoons. We also can not say beer. We would like to use our main label found at www.rollinkites-example.com
Several ideas include having small images of beer cans and beer mugs all over the can as a background. Another idea is to make it freedom and liberty themed. We want to make sure people understand it is a beer, even though we can say beer on the can.

Target Market(s)

30-50 year olds

Industry/Entity Type

THC beverage

Logo Text

Rollin’ Kites Copper Tide

Colors
59FF00
82FF00
B8FF75
E3FFCB
F4FFEA

Requirements
Must have
• Full 12 oz beer can design
Should not have
• No word beer, do not need a new logo, need a can design

```html
<!DOCTYPE html>
<html lang="en">
<head>
<meta charset="utf-8">
<title>Rollin’ Kites Copper Tide – Can Wrap</title>
<link rel="stylesheet" href="https://fonts.googleapis.com/css2?family=Bebas+Neue&family=Oswald:wght@400;600;700&family=Sacramento&display=swap">
<style>
  :root {
    --backdrop: #213528;
    --wrap-white: #ffffff;
    --ink-black: #141414;
    --ink-dark: #1d3a22;
    --ink-green: #2f9a3c;
    --lime-soft: #b8ff75;
    --mint: #e3ffcb;
    --mint-pale: #f4ffea;
    --outline-green: #8fcf86;
    --tone-green: #d4f5b8;
    --tone-orange: #ffe0b8;
    --tone-red: #ffd6cc;
  }
  * { box-sizing: border-box; margin: 0; padding: 0; }
  html, body { width: 1200px; height: 1132px; overflow: hidden; }
  body { background: var(--backdrop); position: relative; font-family: "Oswald", sans-serif; }

  .can-wrap {
    position: absolute; left: 40px; top: 282px;
    width: 1120px; height: 567px;
    overflow: hidden; background: var(--wrap-white);
  }
  .confetti-pattern { position: absolute; inset: 0; width: 100%; height: 100%; }

  .front-panel, .flavor-panel { position: absolute; top: 0; width: 340px; height: 100%; }
  .front-panel { left: 17px; }
  .flavor-panel { left: 762px; }

  .strength-tag {
    position: absolute; top: 74px; width: 100%; text-align: center;
    font-family: "Bebas Neue", "Oswald", sans-serif; font-size: 42px; line-height: 1;
    color: var(--ink-dark); letter-spacing: 1px;
  }
  .flavor-name {
    position: absolute; top: 62px; width: 100%; text-align: center;
    font-family: "Sacramento", cursive; font-size: 50px; line-height: 1;
    color: var(--ink-black); -webkit-text-stroke: 0.8px var(--ink-black);
  }

  .brand-mark {
    position: absolute; left: 20px; width: 300px; height: 300px;
    border-radius: 50%; background: var(--mint);
    display: flex; flex-direction: column; align-items: center; justify-content: center; gap: 14px;
  }
  .front-panel .brand-mark { top: 137px; }
  .flavor-panel .brand-mark { top: 131px; }
  .brand-dot { width: 22px; height: 22px; border-radius: 50%; background: var(--ink-green); }
  .brand-name {
    font-family: "Oswald", sans-serif; font-weight: 700; font-size: 34px; line-height: 1.05;
    color: var(--ink-black); text-align: center; text-transform: uppercase;
  }

  .tagline {
    position: absolute; top: 466px; width: 100%; text-align: center;
    font-family: "Oswald", sans-serif; font-weight: 600; font-style: italic; font-size: 29px;
    color: var(--ink-green); letter-spacing: 0.5px; text-transform: uppercase;
  }
  .dose {
    position: absolute; top: 458px; width: 100%; text-align: center;
    font-family: "Bebas Neue", "Oswald", sans-serif; font-size: 48px; color: var(--mint-pale);
    -webkit-text-stroke: 1.5px var(--outline-green); letter-spacing: 1px;
  }

  .info-panel {
    position: absolute; left: 426px; top: 81px; width: 135px; height: 420px;
    background: var(--wrap-white); padding: 22px 12px 0 12px;
    font-size: 8.4px; line-height: 1.6; color: var(--ink-green); text-transform: uppercase;
  }
  .info-panel h2 { font-size: 8.4px; font-weight: 400; margin-bottom: 14px; }
  .info-panel p { margin-bottom: 12px; }

  .story-panel {
    position: absolute; left: 598px; top: 45px; width: 108px; height: 480px;
    background: var(--wrap-white);
  }
  .story-text {
    position: absolute; inset: 0; writing-mode: vertical-rl; transform: rotate(180deg);
    font-family: "Sacramento", cursive; font-size: 18px; line-height: 21px; color: #222;
    padding: 4px 2px;
  }
</style>
</head>
<body>
  <section class="can-wrap">
    <svg class="confetti-pattern" role="img" aria-label="Repeating confetti pattern of small green, orange and red cans, mugs and squiggles across the whole wrap" viewBox="0 0 1120 567" preserveAspectRatio="none">
      <defs>
        <linearGradient id="confettiTone" x1="0" y1="0" x2="1" y2="1">
          <stop offset="0" stop-color="#f4ffea"/>
          <stop offset="0.3" stop-color="#ffe9cf"/>
          <stop offset="0.55" stop-color="#e3f9cc"/>
          <stop offset="0.8" stop-color="#ffe2da"/>
          <stop offset="1" stop-color="#def7c4"/>
        </linearGradient>
      </defs>
      <rect width="1120" height="567" fill="url(#confettiTone)"/>
    </svg>

    <div class="front-panel">
      <div class="strength-tag">THC</div>
      <div class="brand-mark">
        <span class="brand-dot"></span>
        <span class="brand-name">Rollin’ Kites<br>Copper Tide</span>
      </div>
      <div class="tagline">Teste the new buzz</div>
    </div>

    <div class="info-panel">
      <h2>Ingredients:</h2>
      <p>Filtered water, malted barley, hops, natural flavors, citric acid and hemp extract blended for a crisp, balanced, easy drinking taste. Brewed in small batches, cold filtered and canned fresh to keep every sip bright, clean and full of flavor.</p>
      <p>Contains 10 mg THC per can. Start low and go slow. Effects may take up to two hours to be felt. Do not drive or operate machinery after drinking. Store cold and enjoy responsibly with friends.</p>
      <p>Keep out of reach of children and pets. For adults 21 and over only. Not for sale to minors.</p>
    </div>

    <div class="story-panel">
      <p class="story-text">Brewed without alcohol and crafted for good company, this copper ale pours smooth and finishes clean. Chill it down, crack it open and share it with friends on the porch, at the lake or around the fire. Light body, gentle hops and a calm, easy buzz make every evening a little slower and every conversation a little longer. Raise a can to freedom.</p>
    </div>

    <div class="flavor-panel">
      <div class="flavor-name">Run Punch</div>
      <div class="brand-mark">
        <span class="brand-dot"></span>
        <span class="brand-name">Rollin’ Kites<br>Copper Tide</span>
      </div>
      <div class="dose">10 MG</div>
    </div>
  </section>
</body>
</html>
```